Brantley Advisory Group provides support for renewable energy projects to utilities and suppliers

I need a professional looking business card that is both simple and elegant and unique. My clients are mostly large organizations not individuals. I am a consultant with my own company that is small but would like to give clients the impression I am larger. Smart grid, fiber optics, software, field hardware, distribution automation, substation automation, operations, energy storage/batteries, microgrids, customer service, strategy/roadmaps, conservation, Automated Metering Infrastruture (AMI or smart meters) are all areas of focus.

Target Market(s)

Utilities, suppliers, governmental agencies involved in energy. All types of energy especially natural gas and electrical. Especially renewable energy or green projects.

Contact Information for Business Card

Name - Mark Brantley Cell Phone - 425.318.2746 Email - mbrantley@brantleyag-example.com
Company - Brantley Advisory Group (logo) Title - Principal

Font styles to use
Serif
Sans Serif

Colors

Designer to choose colors to be used in the design.

Requirements
Must have
• Simple and professional and powerful.
• Unique/creative design.
Nice to have
• Utilize color scheme to accent logo colors. Maybe some geometric pattern on edge of card with color.
Should not have
• Busy, complicated, traditional

```html
<!DOCTYPE html>
<html lang="en">
<head>
<meta charset="utf-8">
<title>Brantley Advisory Group – Business Card</title>
<link rel="stylesheet" href="https://fonts.googleapis.com/css2?family=Lato:wght@400;700&family=Merriweather:wght@900&family=Montserrat:wght@400;600&display=swap">
<style>
  :root {
    --backdrop: #262626;
    --card: #111112;
    --card-edge: #1b1b1d;
    --green: #5f8f3b;
    --blue: #2421b8;
    --text-light: #ececec;
    --text-muted: #cfcfcf;
  }
  html, body {
    margin: 0;
    padding: 0;
    width: 1200px;
    height: 853px;
    overflow: hidden;
    background: var(--backdrop);
  }
  .sheet {
    position: relative;
    width: 1200px;
    height: 853px;
    display: flex;
    align-items: center;
    justify-content: center;
    gap: 40px;
  }
  .card {
    position: relative;
    width: 540px;
    height: 308px;
    border-radius: 16px;
    background: linear-gradient(160deg, var(--card-edge) 0%, var(--card) 60%);
    box-shadow: 0 10px 28px rgba(0,0,0,0.55);
    box-sizing: border-box;
    overflow: hidden;
  }
  .brand {
    display: flex;
    align-items: center;
    justify-content: center;
    gap: 12px;
  }
  .brand-mark {
    width: 22px;
    height: 22px;
    background: var(--blue);
    flex: none;
  }
  .brand-name {
    font-family: "Montserrat", sans-serif;
    font-weight: 600;
    font-size: 25px;
    color: var(--green);
    letter-spacing: 0.3px;
    white-space: nowrap;
  }

  /* Front: services */
  .card-front .brand { position: absolute; top: 96px; left: 0; right: 0; }
  .services {
    position: absolute;
    left: 20px;
    right: 20px;
    bottom: 38px;
    font-family: "Lato", sans-serif;
    font-size: 11.5px;
    color: var(--text-light);
    text-align: center;
    line-height: 1.9;
  }
  .services-row { display: block; white-space: nowrap; }
  .service::before {
    content: "";
    display: inline-block;
    width: 5px;
    height: 5px;
    border-radius: 50%;
    background: var(--green);
    margin: 0 4px 2px 6px;
    vertical-align: middle;
  }
  .service:first-child::before { margin-left: 0; }

  /* Back: contact */
  .card-back { text-align: center; }
  .card-back .brand { margin-top: 42px; }
  .person-name {
    margin: 26px 0 0;
    font-family: "Merriweather", serif;
    font-weight: 900;
    font-size: 23px;
    color: var(--green);
  }
  .person-title {
    margin: 4px 0 0;
    font-family: "Montserrat", sans-serif;
    font-size: 13px;
    color: var(--text-light);
    letter-spacing: 0.5px;
  }
  .divider {
    width: 22px;
    height: 2px;
    background: var(--blue);
    margin: 8px auto 10px;
  }
  .contact-icons {
    display: flex;
    justify-content: center;
    gap: 8px;
    margin-bottom: 9px;
  }
  .contact-icon { width: 16px; height: 16px; }
  .contact-list {
    list-style: none;
    margin: 0;
    padding: 0;
    font-family: "Montserrat", sans-serif;
    font-size: 12.5px;
    color: var(--text-muted);
    line-height: 1.5;
  }
</style>
</head>
<body>
<main class="sheet">

  <section class="card card-front" aria-label="Card front">
    <div class="brand">
      <span class="brand-mark"></span>
      <span class="brand-name">Brantley Advisory Group</span>
    </div>
    <div class="services">
      <span class="services-row"><span class="service">Smart Grid</span> <span class="service">Fiber optics</span> <span class="service">Software</span> <span class="service">Field hardware</span> <span class="service">Distribution automation</span></span>
      <span class="services-row"><span class="service">substation automation</span> <span class="service">Operations</span> <span class="service">Energy storage</span> <span class="service">Microgrids</span> <span class="service">Customer service</span></span>
    </div>
  </section>

  <section class="card card-back" aria-label="Card back">
    <div class="brand">
      <span class="brand-mark"></span>
      <span class="brand-name">Brantley Advisory Group</span>
    </div>
    <h1 class="person-name">Mark Brantley</h1>
    <p class="person-title">Principal</p>
    <div class="divider"></div>
    <div class="contact-icons">
      <svg class="contact-icon" viewBox="0 0 16 16" aria-label="Phone">
        <circle cx="8" cy="8" r="8" fill="var(--green)"/>
        <path d="M5.2 4.2l1.4-.3.8 1.8-.9.7c.4.9 1.1 1.7 2 2.1l.7-.9 1.8.8-.3 1.4c-3 .3-5.8-2.6-5.5-5.6z" fill="#fff"/>
      </svg>
      <svg class="contact-icon" viewBox="0 0 16 16" aria-label="Email">
        <circle cx="8" cy="8" r="8" fill="var(--green)"/>
        <rect x="4" y="5.2" width="8" height="5.6" fill="#fff"/>
        <path d="M4 5.2l4 3.2 4-3.2" fill="none" stroke="var(--green)" stroke-width="0.9"/>
      </svg>
      <svg class="contact-icon" viewBox="0 0 16 16" aria-label="Website">
        <circle cx="8" cy="8" r="8" fill="var(--green)"/>
        <circle cx="8" cy="8" r="4" fill="none" stroke="#fff" stroke-width="1"/>
        <ellipse cx="8" cy="8" rx="1.7" ry="4" fill="none" stroke="#fff" stroke-width="0.8"/>
        <line x1="4" y1="8" x2="12" y2="8" stroke="#fff" stroke-width="0.8"/>
      </svg>
    </div>
    <ul class="contact-list">
      <li>425.318.2746</li>
      <li>mbrantley@brantleyag-example.com</li>
      <li>www.brantleyag-example.com</li>
    </ul>
  </section>

</main>
</body>
</html>
```